School Wide Powerpoint design

We are looking to have a powerpoint template created that can be used across the organization for presentation. It must be in brand (see guidelines attached)

Target Market(s)

Board meetings, prospective families, donors, school community

Colors

Designer to choose colors to be used in the design.

Requirements
Must have
• In brand (Fonts \ colors)

```html
<!DOCTYPE html>
<html lang="en">
<head>
<meta charset="utf-8">
<title>Linden Grove School – Presentation Template</title>
<link href="https://fonts.googleapis.com/css2?family=Libre+Baskerville:wght@400;700&family=Poppins:wght@400;500;600;700&display=swap" rel="stylesheet">
<style>
:root{
  --navy:#1f3350;
  --navy-deep:#18293f;
  --gold:#d8b731;
  --red:#ec4a36;
  --grey:#8e8e8e;
  --grey-dark:#5c5c5c;
  --line:#d8d8d8;
  --row:#d2d2d2;
  --ink:#333333;
  --paper:#ffffff;
  --stage:#111111;
}
*{box-sizing:border-box;margin:0;padding:0}
html,body{width:1200px;height:937px;overflow:hidden;background:var(--stage)}
.canvas{position:relative;width:1200px;height:937px;background:var(--stage)}
.slide{position:absolute;width:384px;height:216px;background:var(--paper);overflow:hidden;font-family:"Poppins",sans-serif;color:var(--ink)}
.c1{left:16px}.c2{left:408px}.c3{left:800px}
.r1{top:23px}.r2{top:248px}.r3{top:473px}.r4{top:698px}
.abs{position:absolute}
.serif{font-family:"Libre Baskerville",serif}
svg.layer{position:absolute;left:0;top:0;width:384px;height:216px}

/* shared slide chrome */
.footer{position:absolute;left:0;bottom:0;width:100%;height:11px;background:var(--navy)}
.footer .copy{position:absolute;left:6px;top:2px;font-size:4.5px;color:var(--paper);font-weight:500}
.footer .page{position:absolute;right:0;top:0;width:80px;height:11px;background:var(--gold);clip-path:polygon(12% 0,100% 0,100% 100%,20% 100%);font-size:4.5px;color:var(--paper);text-align:right;padding:3px 8px 0 0}
.footer .notch{position:absolute;right:72px;top:0;width:14px;height:11px;background:var(--paper);clip-path:polygon(0 0,55% 0,100% 100%,45% 100%)}
.mark{position:absolute;top:4px;right:6px;font-family:"Libre Baskerville",serif;font-size:6px;line-height:6.5px;color:var(--navy);text-align:right;letter-spacing:.2px}
.heading{position:absolute;left:10px;top:8px;font-family:"Libre Baskerville",serif;font-size:11px;color:var(--navy);letter-spacing:.2px}
.body-copy{font-size:4.2px;line-height:6.4px;color:var(--grey-dark)}

/* cover */
.cover-title{left:31px;top:70px;font-family:"Libre Baskerville",serif;font-weight:700;font-size:17px;color:var(--paper)}
.cover-sub{left:31px;top:96px;font-family:"Libre Baskerville",serif;font-size:7.5px;color:#dfe3ea}
.cover-mark{left:28px;top:176px;font-family:"Libre Baskerville",serif;font-size:12px;line-height:14px;color:var(--navy)}

/* title slide */
.hero-mark{left:30px;top:150px;font-family:"Libre Baskerville",serif;font-size:18px;line-height:21px;color:var(--navy)}
.hero-title{left:232px;top:168px;font-family:"Libre Baskerville",serif;font-size:15px;color:var(--gold)}
.hero-sub{left:232px;top:193px;font-family:"Libre Baskerville",serif;font-size:7.5px;color:var(--paper)}

/* divider */
.divider-bg{position:absolute;inset:0;background:linear-gradient(100deg,#1f3350 0%,#2b405c 55%,#3a4c63 100%)}
.divider-mark{left:20px;top:66px;font-family:"Libre Baskerville",serif;font-size:11px;line-height:12px;color:var(--paper)}
.divider-title{left:20px;top:108px;font-family:"Libre Baskerville",serif;font-weight:700;font-size:14.5px;color:var(--gold)}
.divider-sub{left:20px;top:132px;font-family:"Libre Baskerville",serif;font-size:7.5px;color:var(--paper)}

/* partners */
.partners-title{left:24px;top:32px;font-family:"Libre Baskerville",serif;font-size:13px;color:var(--navy)}
.partners-intro{left:24px;top:50px;width:190px}
.value{position:absolute;left:24px;width:150px}
.value .num{position:absolute;left:0;top:0;width:13px;height:13px;background:var(--navy);border-radius:3px;color:var(--paper);font-size:5px;font-weight:700;text-align:center;line-height:13px}
.value .label{position:absolute;left:21px;top:-2px;font-size:5.5px;font-weight:600;color:var(--navy)}
.value .text{position:absolute;left:21px;top:6px;width:120px;font-size:3.6px;line-height:5px;color:var(--grey-dark)}

/* pricing */
.plan{position:absolute;top:55px;width:76px;height:125px;border:1px solid;border-radius:5px;text-align:center;background:var(--paper)}
.plan .price{margin-top:10px;font-family:"Libre Baskerville",serif;font-weight:700;font-size:11px;color:var(--ink)}
.plan .band{margin:7px -1px 0;height:8px;color:var(--paper);font-size:3.4px;font-weight:700;line-height:8px;letter-spacing:.2px}
.plan ul{list-style:none;margin-top:8px;font-size:3.6px;line-height:8px;color:var(--grey-dark)}
.plan .tip{position:absolute;left:34px;bottom:-5px;width:8px;height:8px;background:var(--paper);border-right:1px solid;border-bottom:1px solid;transform:rotate(45deg)}
.plan.navy{border-color:var(--navy)} .plan.navy .band{background:var(--navy)} .plan.navy .tip{border-color:var(--navy)}
.plan.gold{border-color:var(--gold)} .plan.gold .band{background:var(--gold)} .plan.gold .tip{border-color:var(--gold)}
.plan.red{border-color:var(--red)} .plan.red .band{background:var(--red)} .plan.red .tip{border-color:var(--red)}
.plan.grey{border-color:var(--grey-dark)} .plan.grey .band{background:var(--grey-dark)} .plan.grey .tip{border-color:var(--grey-dark)}

/* step diagram labels */
.step-title{position:absolute;font-size:5.5px;font-weight:600}
.step-text{position:absolute;width:78px;font-size:3.3px;line-height:4.4px;color:var(--grey-dark)}
.pct{position:absolute;font-size:5px;font-weight:700}

/* table slide */
.col{position:absolute;top:54px;width:68px;text-align:center}
.col .head{height:11px;border-radius:2px;color:var(--paper);font-size:4.6px;font-weight:700;line-height:11px}
.col .amount{margin-top:4px;font-size:7px;font-weight:700;color:var(--ink)}
.col .cell{height:11px;margin-top:2px;font-size:4px;line-height:11px;color:var(--ink)}
.col .cell:nth-of-type(odd){background:var(--row)}
.col .bar{height:5px;margin-top:13px;border-radius:1px}

/* org chart */
.node{position:absolute;height:24px;color:var(--paper);font-size:6.5px;font-weight:600;text-align:center;line-height:24px}

/* graph slide */
.graph-title{left:24px;top:58px;font-family:"Poppins",sans-serif;font-weight:600;font-size:11.5px;color:var(--ink)}
.graph-copy{left:24px;width:150px}
.axis-label{position:absolute;top:182px;font-size:4.4px;color:var(--ink)}

/* process slide */
.ribbon{position:absolute;left:193px;width:152px;height:36px;padding:7px 12px 0 16px}
.ribbon .rt{font-size:4.3px;font-weight:600;color:var(--paper)}
.ribbon .rd{margin-top:2px;font-size:3.3px;line-height:4.4px;color:var(--paper)}

/* quote slide */
.quote-title{left:196px;top:50px;font-weight:700;font-size:13px;color:var(--navy);letter-spacing:.2px}
.quote-text{left:196px;top:68px;width:175px;font-size:4.2px;line-height:6.3px;color:var(--grey-dark);text-align:justify}
.quote-mark{font-family:"Libre Baskerville",serif;font-weight:700;color:#9a9a9a;font-size:56px;line-height:56px}

/* services */
.services-title{left:10px;top:9px;font-family:"Libre Baskerville",serif;font-size:12px;color:var(--red)}
.services-title span{color:var(--navy)}
.service{position:absolute;width:104px;height:80px;border:1px solid #ececec;border-radius:10px;text-align:center}
.service .badge{width:16px;height:16px;margin:8px auto 0;background:var(--navy);border-radius:4px;color:var(--paper);font-size:5.5px;font-weight:700;line-height:16px}
.service .name{margin-top:6px;font-size:5.5px;font-weight:500;color:var(--ink)}
.service .desc{margin:3px 8px 0;font-size:3.6px;line-height:5.2px;color:var(--grey-dark)}
</style>
</head>
<body>
<main class="canvas">

  <!-- 1 cover -->
  <section class="slide c1 r1" aria-label="Cover slide">
    <svg class="layer" viewBox="0 0 384 216" aria-hidden="true">
      <path d="M0 0H384V126C330 150 280 108 220 118C150 130 90 176 0 150Z" fill="var(--navy)"/>
      <path d="M0 150C90 176 150 130 220 118C280 108 330 150 384 126V134C330 158 280 116 220 126C150 138 90 184 0 158Z" fill="var(--gold)"/>
      <rect x="0" y="212" width="384" height="4" fill="var(--grey)"/>
    </svg>
    <div class="abs cover-title">Project Title here</div>
    <div class="abs cover-sub">Subtext here</div>
    <div class="abs cover-mark">LINDEN GROVE<br>SCHOOL</div>
  </section>

  <!-- 2 title -->
  <section class="slide c2 r1" aria-label="Title slide">
    <svg class="layer" viewBox="0 0 384 216">
      <polygon points="262,0 384,0 384,216 200,216" fill="var(--navy)"/>
      <polygon points="253,0 262,0 200,216 191,216" fill="var(--gold)"/>
      <polygon points="30,82 36,82 51,28 45,28" fill="var(--red)"/>
      <g role="img" aria-label="Photo strip of students learning and smiling in class">
        <polygon points="42,82 122,82 137,28 57,28" fill="#8a6b52"/>
        <polygon points="126,82 178,82 193,28 141,28" fill="#a7564a"/>
        <polygon points="182,82 262,82 277,28 197,28" fill="#6f7f86"/>
        <polygon points="266,82 352,82 367,28 281,28" fill="#b98a4e"/>
      </g>
    </svg>
    <div class="abs hero-mark">LINDEN GROVE<br>SCHOOL</div>
    <div class="abs hero-title">Project Title here</div>
    <div class="abs hero-sub">Subtext here</div>
  </section>

  <!-- 3 divider -->
  <section class="slide c3 r1" aria-label="Section divider slide">
    <div class="divider-bg" role="img" aria-label="Faded photo of students in a science class"></div>
    <div class="abs divider-mark">LINDEN GROVE<br>SCHOOL</div>
    <div class="abs divider-title">SECTION DEVIDER HERE</div>
    <div class="abs divider-sub">Subtext here</div>
  </section>

  <!-- 4 partners -->
  <section class="slide c1 r2" aria-label="Partners slide">
    <div class="mark">LINDEN GROVE<br>SCHOOL</div>
    <div class="abs partners-title">OUR PARTNERS</div>
    <p class="abs partners-intro body-copy">Lorem ipsum dolor sit amet, consectetur adipiscing elit, sed do eiusmod tempor incididunt ut labore et dolore magna aliqua.</p>
    <div class="value" style="top:80px"><div class="num">01</div><div class="label">Experience</div><div class="text">Lorem ipsum dolor sit amet, consectetur adipiscing elit, sed do eiusmod tempor incididunt ut labore aliqua.</div></div>
    <div class="value" style="top:112px"><div class="num">02</div><div class="label">Excellence</div><div class="text">Lorem ipsum dolor sit amet, consectetur adipiscing elit, sed do eiusmod tempor incididunt ut labore aliqua.</div></div>
    <div class="value" style="top:144px"><div class="num">03</div><div class="label">Effective</div><div class="text">Dolor sit amet, consectetur adipiscing elit, sed do eiusmod tempor incididunt ut labore aliqua.</div></div>
    <svg class="layer" viewBox="0 0 384 216">
      <g fill="var(--paper)" stroke="#e2e2e2" stroke-width="1">
        <polygon points="243,20 270.7,36 270.7,68 243,84 215.3,68 215.3,36"/>
        <polygon points="304,20 331.7,36 331.7,68 304,84 276.3,68 276.3,36"/>
        <polygon points="212,78 239.7,94 239.7,126 212,142 184.3,126 184.3,94"/>
        <polygon points="273,78 300.7,94 300.7,126 273,142 245.3,126 245.3,94"/>
        <polygon points="335,78 362.7,94 362.7,126 335,142 307.3,126 307.3,94"/>
        <polygon points="243,136 270.7,152 270.7,184 243,200 215.3,184 215.3,152"/>
        <polygon points="304,136 331.7,152 331.7,184 304,200 276.3,184 276.3,152"/>
      </g>
      <g fill="#c9ccd2">
        <rect x="228" y="47" width="30" height="10" rx="2" role="img" aria-label="Partner badge"/>
        <rect x="292" y="44" width="24" height="16" rx="2" role="img" aria-label="Partner badge"/>
        <rect x="197" y="105" width="30" height="10" rx="2" role="img" aria-label="Partner badge"/>
        <rect x="256" y="105" width="34" height="10" rx="2" role="img" aria-label="Partner badge"/>
        <circle cx="335" cy="110" r="11" role="img" aria-label="Partner badge"/>
        <rect x="233" y="156" width="20" height="24" rx="2" role="img" aria-label="Partner badge"/>
        <rect x="288" y="162" width="32" height="12" rx="2" role="img" aria-label="Partner badge"/>
      </g>
    </svg>
    <div class="footer"><span class="copy">Copyright text here</span><span class="notch"></span><span class="page">Page : 01</span></div>
  </section>

  <!-- 5 pricing -->
  <section class="slide c2 r2" aria-label="Pricing slide">
    <div class="heading">SECTION TITLE HERE</div>
    <div class="mark">LINDEN GROVE<br>SCHOOL</div>
    <div class="plan navy" style="left:26px"><div class="price">$49</div><div class="band">PERSONAL</div><ul><li>20 GB Bandwidth</li><li>Financ Analysing</li><li>Daily 15 Reports</li><li>12 Team Members</li><li>24 hour support</li></ul><span class="tip"></span></div>
    <div class="plan gold" style="left:113px"><div class="price">$75</div><div class="band">PROFESSIONAL</div><ul><li>20 GB Bandwidth</li><li>Financ Analysing</li><li>Daily 15 Reports</li><li>12 Team Members</li><li>24 hour support</li></ul><span class="tip"></span></div>
    <div class="plan red" style="left:200px"><div class="price">$85</div><div class="band">SMALL BUSINESS</div><ul><li>20 GB Bandwidth</li><li>Financ Analysing</li><li>Daily 15 Reports</li><li>12 Team Members</li><li>24 hour support</li></ul><span class="tip"></span></div>
    <div class="plan grey" style="left:287px"><div class="price">$99</div><div class="band">STARTUP</div><ul><li>20 GB Bandwidth</li><li>Financ Analysing</li><li>Daily 15 Reports</li><li>12 Team Members</li><li>24 hour support</li></ul><span class="tip"></span></div>
    <div class="footer"><span class="copy">Copyright text here</span><span class="notch"></span><span class="page">Page : 01</span></div>
  </section>

  <!-- 6 step diagram -->
  <section class="slide c3 r2" aria-label="Step diagram slide">
    <div class="heading">GRAPHICS TITLE HERE</div>
    <div class="mark">LINDEN GROVE<br>SCHOOL</div>
    <svg class="layer" viewBox="0 0 384 216">
      <defs><clipPath id="disc"><circle cx="196" cy="109" r="64"/></clipPath></defs>
      <g clip-path="url(#disc)">
        <rect x="120" y="40" width="160" height="36" fill="var(--red)"/>
        <rect x="120" y="78" width="160" height="30" fill="var(--navy)"/>
        <rect x="120" y="110" width="160" height="30" fill="var(--gold)"/>
        <rect x="120" y="142" width="160" height="40" fill="var(--grey)"/>
      </g>
      <g stroke="var(--paper)" stroke-width=".8">
        <line x1="193" y1="56" x2="193" y2="68"/><line x1="193" y1="87" x2="193" y2="99"/>
        <line x1="193" y1="119" x2="193" y2="131"/><line x1="193" y1="151" x2="193" y2="163"/>
      </g>
      <g fill="var(--paper)">
        <circle cx="182" cy="62" r="4"/><circle cx="182" cy="93" r="3.5" fill="none" stroke="var(--paper)" stroke-width="1.2"/>
        <path d="M182 119v10M178 126q4 5 8 0M180 121h4" stroke="var(--paper)" stroke-width="1.2" fill="none"/>
        <circle cx="182" cy="157" r="4"/>
      </g>
      <g font-family="Poppins" font-size="5.5" font-weight="600" fill="var(--paper)">
        <text x="198" y="60">Step</text><text x="198" y="67">04</text>
        <text x="198" y="91">Step</text><text x="198" y="98">03</text>
        <text x="198" y="123">Step</text><text x="198" y="130">02</text>
        <text x="198" y="155">Step</text><text x="198" y="162">01</text>
      </g>
      <g fill="none" stroke-width="1.6">
        <path d="M140 60A74 74 0 0 1 250 47" stroke="var(--red)"/>
        <path d="M268 95A74 74 0 0 1 262 140" stroke="var(--gold)"/>
        <path d="M128 78A74 74 0 0 0 124 120" stroke="var(--navy)"/>
        <path d="M150 166A74 74 0 0 0 176 178" stroke="var(--grey)"/>
      </g>
      <g stroke-width=".8" fill="none">
        <path d="M250 50H280" stroke="var(--red)"/><path d="M276 47l4 3-4 3" stroke="var(--red)"/>
        <path d="M262 136H290" stroke="var(--gold)"/><path d="M286 133l4 3-4 3" stroke="var(--gold)"/>
        <path d="M124 97H96" stroke="var(--navy)"/><path d="M100 94l-4 3 4 3" stroke="var(--navy)"/>
        <path d="M150 166H124" stroke="var(--grey)"/><path d="M128 163l-4 3 4 3" stroke="var(--grey)"/>
      </g>
      <g>
        <rect x="328" y="80" width="3" height="16" fill="var(--red)"/><rect x="332" y="82" width="12" height="2" fill="var(--red)"/><rect x="332" y="86" width="8" height="2" fill="#cfcfcf"/><rect x="332" y="90" width="10" height="2" fill="#cfcfcf"/>
        <rect x="38" y="84" width="3" height="16" fill="var(--navy)"/><rect x="42" y="86" width="10" height="2" fill="#cfcfcf"/><rect x="42" y="90" width="7" height="2" fill="#cfcfcf"/><rect x="42" y="94" width="9" height="2" fill="#cfcfcf"/>
        <rect x="62" y="157" width="3" height="16" fill="var(--grey)"/><rect x="66" y="159" width="10" height="2" fill="#cfcfcf"/><rect x="66" y="163" width="7" height="2" fill="#cfcfcf"/><rect x="66" y="167" width="9" height="2" fill="#cfcfcf"/>
        <rect x="330" y="166" width="3" height="16" fill="var(--gold)"/><rect x="334" y="168" width="10" height="2" fill="#cfcfcf"/><rect x="334" y="172" width="7" height="2" fill="#cfcfcf"/><rect x="334" y="176" width="9" height="2" fill="#cfcfcf"/>
      </g>
    </svg>
    <div class="step-title" style="left:282px;top:46px;color:var(--red)">Title Four</div>
    <div class="step-text" style="left:282px;top:54px">Nam pretium turpis et arcu. Duis arcu tortor, suscipit eget, imperdiet nec, imperdiet iaculis, ipsum. Sed aliquam ultrices mauris.</div>
    <div class="pct" style="left:310px;top:81px;color:var(--red)">45%</div>
    <div class="step-title" style="left:292px;top:131px;color:var(--gold)">Title Two</div>
    <div class="step-text" style="left:292px;top:139px">Nam pretium turpis et arcu. Duis arcu tortor, suscipit eget, imperdiet nec, imperdiet iaculis, ipsum. Sed aliquam ultrices mauris.</div>
    <div class="pct" style="left:311px;top:170px;color:var(--gold)">15%</div>
    <div class="step-title" style="left:56px;top:94px;color:var(--navy)">Title Three</div>
    <div class="step-text" style="left:14px;top:102px;text-align:center">Nam pretium turpis et arcu. Duis arcu tortor, suscipit eget, imperdiet nec, imperdiet iaculis, ipsum. Sed aliquam ultrices mauris.</div>
    <div class="pct" style="left:18px;top:84px;color:var(--navy)">25%</div>
    <div class="step-title" style="left:84px;top:163px;color:var(--grey)">Title One</div>
    <div class="step-text" style="left:36px;top:172px;text-align:center">Nam pretium turpis et arcu. Duis arcu tortor, suscipit eget, imperdiet nec, imperdiet iaculis, ipsum. Sed aliquam ultrices mauris.</div>
    <div class="pct" style="left:42px;top:163px;color:var(--grey)">35%</div>
    <div class="footer"><span class="copy">Copyright text here</span><span class="notch"></span><span class="page">Page : 01</span></div>
  </section>

  <!-- 7 table -->
  <section class="slide c1 r3" aria-label="Table slide">
    <div class="heading">TABLE SLIDE TITLE HERE</div>
    <div class="mark">LINDEN GROVE<br>SCHOOL</div>
    <div class="col" style="left:29px"><div class="head" style="background:var(--gold)">TABLE TITLE HERE</div><div class="amount">$0000</div><div class="cell">Text here</div><div class="cell">Text here</div><div class="cell">Text here</div><div class="cell">Text here</div><div class="cell">Text here</div><div class="cell">Text here</div><div class="bar" style="background:var(--gold)"></div></div>
    <div class="col" style="left:118px"><div class="head" style="background:var(--red)">TABLE TITLE HERE</div><div class="amount">$0000</div><div class="cell">Text here</div><div class="cell">Text here</div><div class="cell">Text here</div><div class="cell">Text here</div><div class="cell">Text here</div><div class="cell">Text here</div><div class="bar" style="background:var(--red)"></div></div>
    <div class="col" style="left:205px"><div class="head" style="background:var(--navy)">TABLE TITLE HERE</div><div class="amount">$0000</div><div class="cell">Text here</div><div class="cell">Text here</div><div class="cell">Text here</div><div class="cell">Text here</div><div class="cell">Text here</div><div class="cell">Text here</div><div class="bar" style="background:var(--navy)"></div></div>
    <div class="col" style="left:292px"><div class="head" style="background:var(--grey-dark)">TABLE TITLE HERE</div><div class="amount">$0000</div><div class="cell">Text here</div><div class="cell">Text here</div><div class="cell">Text here</div><div class="cell">Text here</div><div class="cell">Text here</div><div class="cell">Text here</div><div class="bar" style="background:var(--grey-dark)"></div></div>
    <div class="footer"><span class="copy">Copyright text here</span><span class="notch"></span><span class="page">Page : 01</span></div>
  </section>

  <!-- 8 org chart -->
  <section class="slide c2 r3" aria-label="Hierarchy chart slide">
    <div class="heading" style="color:var(--red)">GRAPHICS TITLE HERE</div>
    <div class="mark">LINDEN GROVE<br>SCHOOL</div>
    <svg class="layer" viewBox="0 0 384 216" aria-hidden="true">
      <g stroke="#9a9a9a" stroke-width="1" fill="none">
        <path d="M190 63V82M96 98V82H279V98"/>
        <path d="M96 122V140M45 156V140H149V156"/>
        <path d="M279 122V140M228 156V140H333V156"/>
      </g>
    </svg>
    <div class="node" style="left:154px;top:39px;width:73px;background:var(--navy)">Main Here</div>
    <div class="node" style="left:65px;top:98px;width:63px;background:var(--gold)">Sub Here</div>
    <div class="node" style="left:248px;top:98px;width:63px;background:var(--gold)">Sub Here</div>
    <div class="node" style="left:15px;top:156px;width:61px;background:var(--red)">Sub Here</div>
    <div class="node" style="left:119px;top:156px;width:61px;background:var(--grey)">Sub Here</div>
    <div class="node" style="left:198px;top:156px;width:61px;background:var(--red)">Sub Here</div>
    <div class="node" style="left:303px;top:156px;width:61px;background:var(--grey)">Sub Here</div>
    <div class="footer"><span class="copy">Copyright text here</span><span class="notch"></span><span class="page">Page : 01</span></div>
  </section>

  <!-- 9 bar chart -->
  <section class="slide c3 r3" aria-label="Graph slide">
    <div class="heading">SECTION TITLE HERE</div>
    <div class="mark">LINDEN GROVE<br>SCHOOL</div>
    <div class="abs graph-title">Graph title here</div>
    <p class="abs graph-copy body-copy" style="top:78px">Lorem ipsum dolor sit amet, consectetur adipiscing elit, sed do eiusmod tempor incididunt ut labore et dolore magna aliqua. Quis ipsum suspendisse ultrices gravida. Risus commodo viverra maecenas accumsan lacus vel facilisis.</p>
    <p class="abs graph-copy body-copy" style="top:132px">Eiusmod tempor incididunt ut labore et dolore magna aliqua. Quis ipsum suspendisse ultrices gravida. Risus commodo viverra maecenas accumsan lacus vel facilisis.</p>
    <svg class="layer" viewBox="0 0 384 216" aria-hidden="true">
      <g fill="var(--navy)">
        <rect x="178" y="105" width="3.5" height="62"/><rect x="202" y="77" width="3.5" height="90"/>
        <rect x="227" y="80" width="3.5" height="87"/><rect x="251" y="67" width="3.5" height="100"/>
        <rect x="276" y="92" width="3.5" height="75"/><rect x="300" y="114" width="3.5" height="53"/>
        <rect x="325" y="58" width="3.5" height="109"/><rect x="349" y="75" width="3.5" height="92"/>
      </g>
      <g fill="var(--gold)">
        <rect x="184" y="128" width="3.5" height="39"/><rect x="208" y="60" width="3.5" height="107"/>
        <rect x="233" y="102" width="3.5" height="65"/><rect x="257" y="62" width="3.5" height="105"/>
        <rect x="282" y="58" width="3.5" height="109"/><rect x="306" y="95" width="3.5" height="72"/>
        <rect x="331" y="45" width="3.5" height="122"/><rect x="355" y="61" width="3.5" height="106"/>
      </g>
    </svg>
    <span class="axis-label" style="left:174px">2012</span><span class="axis-label" style="left:198px">2012</span>
    <span class="axis-label" style="left:223px">2012</span><span class="axis-label" style="left:247px">2012</span>
    <span class="axis-label" style="left:272px">2012</span><span class="axis-label" style="left:296px">2012</span>
    <span class="axis-label" style="left:321px">2012</span><span class="axis-label" style="left:345px">2012</span>
    <div class="footer"><span class="copy">Copyright text here</span><span class="notch"></span><span class="page">Page : 01</span></div>
  </section>

  <!-- 10 process -->
  <section class="slide c1 r4" aria-label="Process slide">
    <div class="mark">LINDEN GROVE<br>SCHOOL</div>
    <div class="abs" style="left:0;top:0;width:145px;height:216px;background:linear-gradient(160deg,#a8744c 0%,#d98a3c 55%,#7b5a44 100%)" role="img" aria-label="Photo of a student writing at a desk"></div>
    <svg class="layer" viewBox="0 0 384 216" aria-hidden="true">
      <g stroke="#b9b9b9" stroke-width=".8" fill="none">
        <path d="M152 84V58H200"/><path d="M178 110H200"/><path d="M152 136V162H200"/>
      </g>
      <circle cx="152" cy="110" r="28" fill="none" stroke="#e6e6e6" stroke-width="5"/>
      <path d="M152 82A28 28 0 0 0 126 128" fill="none" stroke="var(--gold)" stroke-width="3"/>
      <circle cx="152" cy="110" r="21" fill="var(--paper)" stroke="#ececec"/>
      <g fill="none" stroke="var(--red)" stroke-width="1">
        <path d="M148 114q-4-4-4-8a8 8 0 0 1 16 0q0 4-4 8z"/><path d="M149 117h6M150 120h4"/>
        <path d="M152 96v-3M141 100l-2-2M163 100l2-2"/>
      </g>
    </svg>
    <div class="ribbon" style="top:42px;background:var(--gold);clip-path:polygon(0 0,94% 0,100% 50%,94% 100%,0 100%,5% 50%)"><div class="rt">Business Market Research</div><div class="rd">Lorem ipsum dolor sit amet, consectetur adipiscing elit, sed do eiusmod tempor incididunt ut labore.</div></div>
    <div class="ribbon" style="top:92px;background:#272a2f;clip-path:polygon(6% 0,100% 0,95% 50%,100% 100%,6% 100%,0 50%)"><div class="rt">Finding Creative Solutions</div><div class="rd">Lorem ipsum dolor sit amet, consectetur adipiscing elit, sed do eiusmod tempor incididunt ut labore.</div></div>
    <div class="ribbon" style="top:142px;background:var(--red);clip-path:polygon(0 0,94% 0,100% 50%,94% 100%,0 100%,5% 50%)"><div class="rt">Solving Problem With Confident</div><div class="rd">Lorem ipsum dolor sit amet, consectetur adipiscing elit, sed do eiusmod tempor incididunt ut labore.</div></div>
  </section>

  <!-- 11 quotation -->
  <section class="slide c2 r4" aria-label="Quotation slide">
    <div class="mark">LINDEN GROVE<br>SCHOOL</div>
    <svg class="layer" viewBox="0 0 384 216">
      <path d="M0 0H56L224 158Q236 172 222 186L194 216H0Z" fill="#8a7668" role="img" aria-label="Photo of two smiling students sitting outdoors"/>
      <path d="M62 0L230 160Q240 172 228 186" fill="none" stroke="var(--gold)" stroke-width="1.5"/>
    </svg>
    <div class="abs quote-mark" style="left:148px;top:16px">&ldquo;</div>
    <div class="abs quote-mark" style="left:334px;top:118px">&rdquo;</div>
    <div class="abs quote-title">QUATATION TITLE HERE</div>
    <p class="abs quote-text">Lorem ipsum dolor sit amet, consect eturadi piscing elit, sed do eiusmod tempor incid idunt utlabore lorem ipsum dolor sit amet, consect eturadi piscing elit, sed do eiusmod tempor. Lorem ipsum dolor sit amet, consect eturadi piscing elit, sed do eiusmod tempor incid idunt utlabore lorem ipsum dolor sit amet, consect eturadi piscing elit, sed do piscing elit, sed do eiusmod.</p>
    <div class="footer"><span class="copy">Copyright text here</span><span class="notch"></span><span class="page">Page : 01</span></div>
  </section>

  <!-- 12 services -->
  <section class="slide c3 r4" aria-label="Class services slide">
    <div class="abs services-title">OUR CLASS <span>SERVICES</span></div>
    <div class="mark">LINDEN GROVE<br>SCHOOL</div>
    <div class="service" style="left:30px;top:36px"><div class="badge">01</div><div class="name">Services - 01</div><div class="desc">Lorem ipsum dolor sit amet, consectetur adipiscing elit, sed do eiusmod tempor incididunt ut labor aliqua.</div></div>
    <div class="service" style="left:140px;top:36px"><div class="badge">02</div><div class="name">Services - 02</div><div class="desc">Lorem ipsum dolor sit amet, consectetur adipiscing elit, sed do eiusmod tempor incididunt ut labor aliqua.</div></div>
    <div class="service" style="left:250px;top:36px"><div class="badge">03</div><div class="name">Services - 03</div><div class="desc">Lorem ipsum dolor sit amet, consectetur adipiscing elit, sed do eiusmod tempor incididunt ut labor aliqua.</div></div>
    <div class="service" style="left:30px;top:122px"><div class="badge">04</div><div class="name">Services - 04</div><div class="desc">Lorem ipsum dolor sit amet, consectetur adipiscing elit, sed do eiusmod tempor incididunt ut labor aliqua.</div></div>
    <div class="service" style="left:140px;top:122px"><div class="badge">05</div><div class="name">Services - 05</div><div class="desc">Lorem ipsum dolor sit amet, consectetur adipiscing elit, sed do eiusmod tempor incididunt ut labor aliqua.</div></div>
    <div class="service" style="left:250px;top:122px"><div class="badge">06</div><div class="name">Services - 06</div><div class="desc">Lorem ipsum dolor sit amet, consectetur adipiscing elit, sed do eiusmod tempor incididunt ut labor aliqua.</div></div>
    <div class="footer"><span class="notch"></span><span class="page"></span></div>
  </section>

</main>
</body>
</html>
```